Torvex Works CBD Packaging Label Design. Creative Modern Minimalist. Future Work possible!!!

Creating a CBD product.Bottle size is height 84mm diameter 25mmLabel size 74mm x 38mmMatch Stick Box: 40mm x 100mm x 50mm
Pippette cap is red FYI.
NOTE: We have added a logo file but I am also paying for a new logo design. So do as you please.Need the packaging and labelling done for CBD product. Name is Torvex Works. Logo is included in file below. I have also added some product packaging and design for inspiration. No need to use this but to give you an idea. Some flexibility with label dimensions. In so far as, it must fit on the base of the bottle, think eye dropper.

The last velmira cbd oil dropper is a cool industrial design but we would prefer a design with a label.Red and white are the main colors. Minimalist, modern, clean, swiss cross in the mix are acceptable.

Also, the logo image with the textured background on the business card is part of then look we would like to package. Not a requirement but certainly a consideration.Feel free to reach out for any further questions.Below are some specs and text we need to squeeze on then packaging / labelling.

The location of the text or emphasis is NOT fixed even if it specifies the location in the description below.

Box must contain:
logo, torvex Works text
Warnings-(warning sign with exclamation mark) not suitable for consumption -under 18 restricted sign?
PACKAGING TEXT (Classic rectangular)
LogoCanna Labs (below logo)10% CBD Oil (x milligram mg)10ml
Disclaimers (From drovent)
MEDICAL: (From drovent website) Disclaimer: Torvex Works products are sold without any medical claims; they have not been proven to treat, relieve, nor cure any disease or medical condition. please refer to the terms and conditions (need to read these from)
CONTACT: Avoid contact during pregnancy and while nursing. Do not get in eyes, on skin, or on clothing. Get medical advice/attention if you feel unwell.ADVICE: Keep out of reach of children. Protect from sunlight. Store in a well-ventilated place. Keep cool. Refrigerate after opening.
Ingredients: Ingredients: 80% MCT oil, 20% Ferravanta Colmare (What terpenes?check with bright meadow). 100% organic. (Check labeling) Extracted using ethanol extraction.

Side note: More information about boxing size and bottle can be seen on a competitiors site. shown below.

https://drovent.example/product-category/selection/

Target Market(s)

CBD oil users in Europe

Logo Text

torvex works

Font styles to use
Serif
Sans Serif
Script

Requirements
Must have
• I want textured, like business card texture considered for the label. The box is a standard cardboard for the moment. Pharma grade product. I would like it to stand out in a pharmacy but not look out of place.
• We need all sides of the packaging. Use lorem ipsum if you have to. Some of the text is above though
Should not have
• Nothing that references the weed leaf. Keep that off

```html
<!DOCTYPE html>
<html lang="en">
<head>
<meta charset="utf-8">
<title>Torvex Works CBD Oil Packaging</title>
<link rel="stylesheet" href="https://fonts.googleapis.com/css2?family=Oswald:wght@400;500;700&family=Questrial&display=swap">
<style>
  :root {
    --red: #e3232b;
    --white: #ffffff;
    --sand: #d3c2a8;
    --ink: #333333;
    --grey-text: #5a5a5a;
    --bg-top: #2a2a2a;
    --bg-bottom: #f2f2f2;
  }
  * { margin: 0; padding: 0; box-sizing: border-box; }
  html, body { width: 1200px; height: 935px; overflow: hidden; }
  body {
    position: relative;
    background: linear-gradient(to bottom, var(--bg-top) 0%, #8a8a8a 35%, var(--bg-bottom) 75%, #ffffff 100%);
    font-family: "Questrial", sans-serif;
  }

  /* Brand lockup */
  .brand-lockup {
    position: absolute; left: 745px; top: 200px;
    display: flex; align-items: center; gap: 14px;
  }
  .brand-dot { width: 22px; height: 22px; border-radius: 50%; background: var(--red); }
  .brand-name { font-size: 42px; letter-spacing: 4px; color: var(--red); }

  /* Flat panels */
  .panel { position: absolute; background: var(--white); overflow: hidden; }
  .band-top { position: absolute; left: 0; top: 0; width: 100%; height: 22px; background: var(--red); }
  .band-bottom {
    position: absolute; left: 0; bottom: 0; width: 100%; height: 80px; background: var(--red);
    display: flex; align-items: center; justify-content: center;
    font-family: "Oswald", sans-serif; font-weight: 500; font-size: 22px; color: var(--white);
  }

  /* Side panel */
  .box-side { left: 205px; top: 320px; width: 131px; height: 510px; }
  .side-copy { padding: 40px 8px 0 8px; font-family: "Oswald", sans-serif; color: var(--grey-text); }
  .side-heading { color: var(--red); font-size: 10px; font-weight: 500; margin-bottom: 8px; }
  .side-subheading { color: var(--red); font-size: 6px; font-weight: 500; margin: 16px 0 6px; }
  .side-list { list-style: none; font-size: 6px; line-height: 1.55; }
  .side-list li::before { content: "• "; }
  .ingredients-label { color: var(--red); font-size: 6px; margin-top: 12px; }
  .ingredients { font-size: 6px; line-height: 1.5; }

  /* Shared pieces */
  .panel-brand {
    position: absolute; left: 0; width: 100%;
    display: flex; align-items: center; justify-content: center; gap: 5px;
    font-size: 11px; letter-spacing: 1.5px; color: var(--red);
  }
  .panel-brand .mark { width: 6px; height: 6px; border-radius: 50%; background: var(--red); }
  .swiss-cross, .seal, .product-title { position: absolute; display: block; }
  .product-title text { font-family: "Oswald", sans-serif; font-weight: 700; fill: var(--sand); }

  /* Front panel */
  .box-front { left: 336px; top: 320px; width: 160px; height: 510px; }
  .box-front .panel-brand { top: 76px; }
  .box-front .swiss-cross { left: 63px; top: 127px; }
  .box-front .product-title { left: 6px; top: 204px; }
  .box-front .seal { right: 8px; bottom: 92px; }

  /* Bottle label */
  .bottle-label { left: 525px; top: 580px; width: 164px; height: 252px; }
  .bottle-label .panel-brand { top: 40px; font-size: 10px; }
  .bottle-label .product-title { left: 8px; top: 74px; }
  .bottle-label .swiss-cross { left: 117px; top: 104px; }
  .bottle-label .seal { left: 112px; top: 156px; }
  .bottle-label .band-bottom { height: 46px; font-size: 20px; }
</style>
</head>
<body>

  <div class="brand-lockup">
    <span class="brand-dot"></span>
    <span class="brand-name">Torvex Works</span>
  </div>

  <section class="panel box-side">
    <div class="band-top"></div>
    <div class="side-copy">
      <h2 class="side-heading">Medical Benefits of "CBD"</h2>
      <ul class="side-list">
        <li>Pain relief</li><li>Anti-anxiety</li><li>Anti-psychotic</li><li>Muscle relaxant</li>
        <li>Anti-cancer</li><li>Anti-seizure</li><li>Anti-inflammatory</li><li>Neuroprotective</li>
      </ul>
      <h3 class="side-subheading">CBD shows promise in the treatment of several conditions:</h3>
      <ul class="side-list">
        <li>Chronic Pain</li><li>Hepatitis C, especially active disease</li><li>Reduces inflammation and fibrosis</li>
        <li>Psychiatric illness (anxiety, bipolar, schizophrenia)</li><li>Seizure disorders and other central nervous conditions</li>
        <li>Insomnia</li><li>Inflammatory disorders such as rheumatoid arthritis</li>
        <li>Patients who enjoy the benefits of cannabis but don't want psychoactive effects</li>
      </ul>
      <p class="ingredients-label">INGREDIENTS:</p>
      <p class="ingredients">80% MCT oil, 20% cannabis sativa flower extract oil (monoterpenes, sesquiterpenes, terpenophenolics). 100% organic, semi-decarboxylated flower extract oil, cold filtered.</p>
    </div>
    <div class="band-bottom"></div>
  </section>

  <section class="panel box-front">
    <div class="band-top"></div>
    <div class="panel-brand"><span class="mark"></span>Torvex Works</div>
    <svg class="swiss-cross" width="34" height="34" viewBox="0 0 34 34" aria-label="Swiss cross">
      <rect width="34" height="34" fill="var(--red)"/>
      <rect x="14" y="7" width="6" height="20" fill="#fff"/>
      <rect x="7" y="14" width="20" height="6" fill="#fff"/>
    </svg>
    <svg class="product-title" width="150" height="210" viewBox="0 0 150 210" aria-label="CBD Oil">
      <text x="0" y="118" font-size="142" textLength="148" lengthAdjust="spacingAndGlyphs">CBD</text>
      <text x="2" y="200" font-size="78" textLength="60" lengthAdjust="spacingAndGlyphs">OIL</text>
    </svg>
    <svg class="seal" width="46" height="46" viewBox="0 0 46 46" role="img" aria-label="Organic seal">
      <circle cx="23" cy="23" r="20" fill="none" stroke="var(--red)" stroke-width="2"/>
      <circle cx="23" cy="23" r="14" fill="none" stroke="var(--ink)" stroke-width="1"/>
    </svg>
    <div class="band-bottom">50 ml</div>
  </section>

  <section class="panel bottle-label">
    <div class="panel-brand"><span class="mark"></span>Torvex Works</div>
    <svg class="product-title" width="92" height="120" viewBox="0 0 92 120" aria-label="CBD Oil">
      <text x="0" y="76" font-size="90" textLength="88" lengthAdjust="spacingAndGlyphs">CBD</text>
      <text x="2" y="114" font-size="42" textLength="40" lengthAdjust="spacingAndGlyphs">OIL</text>
    </svg>
    <svg class="swiss-cross" width="26" height="26" viewBox="0 0 34 34" aria-label="Swiss cross">
      <rect width="34" height="34" fill="var(--red)"/>
      <rect x="14" y="7" width="6" height="20" fill="#fff"/>
      <rect x="7" y="14" width="20" height="6" fill="#fff"/>
    </svg>
    <svg class="seal" width="40" height="40" viewBox="0 0 46 46" role="img" aria-label="Organic seal">
      <circle cx="23" cy="23" r="20" fill="none" stroke="var(--red)" stroke-width="2"/>
      <circle cx="23" cy="23" r="14" fill="none" stroke="var(--ink)" stroke-width="1"/>
    </svg>
    <div class="band-bottom">50 ml</div>
  </section>

</body>
</html>
```